依頼詳細
◆サイトマップ
01.ホーム
02.当院について
03.医院紹介
04.スタッフ紹介
05.初めての方へ
06.銀歯から自然な白い歯へ
07.歯医者にいけなくなった方へ
08.歯の色を全体的に白くしたい方へ
09.口臭が気になる・歯茎に違和感がある
10.歯並びを整えたい方へ
11.歯が失ってしまった方へ
12.虫歯になってしまった方へ
13.お子様の歯を守りたい方へ
14.求人情報
15.よくあるご質問
16.問い合わせ
17.お知らせ(一覧)
18.お知らせ(詳細)
19.ブログ(一覧)
20.ブログ(詳細)

◆TOPに掲載いただきたいもの
・ヘッダー、ロゴ、営業時間、電話番号
・グローバルナビ
・メインイメージ
・お知らせの新着ボックス
・コンセプト
・強み
・各症状ページへ流入する箇所(サイトマップ06~13の内容)
・その他下層ページ移行用バナー(よくあるご質問、問い合わせ、求人情報)
・ブログの新着ボックス
・グーグルマップ
・フッター(ロゴ、院情報、営業時間、サイトマップ)
※仮で作成したもののためレイアウトの並びはお任せ致します。
ただし、配置してあるコンテンツはすべて含まれるようにしてください。
提案で項目を追加頂く等は参考にさせて頂きたいので大変嬉しいです。

◆デザインについて
・希望するイメージ
知的/清潔な/高級感

・希望デザインカラー
茶系
ベースは白やベージュ系

◆参考URL
https://hirotsudentaloffice.example/
スペースのとり方に高級感を感じとても見やすい印象
TOPのコンテンツ量が少ないと感じる
サイトURL
http://203.0.113.47
ページ数
1ページ
希望イメージ
シンプル 複雑
単色 カラフル
暗い 明るい
日常 高級
遊び心 厳粛
未来的 伝統的
女性的 男性的
希望する色
茶系、ベースは白やベージュ系
納品ファイル
• イラストレーター形式 (.ai)
• フォトショップ形式 (.psd)
補足説明
◆素材について
素材として必要なものがある場合には、Pixmora Stock画像をご使用ください。
その際、通常アセットでダウンロード出来る画像のみを使用してください。
Pixmora Stock以外の素材を使用する際には、
必ず無料で提供いただける物のみご使用ください。
※現在、写真の用意がないのですが、撮影後に差し替える予定です。
イメージとしてPixmora Stock画像を使用して作成ください。

◆ロゴ、外観、内観写真について
下記よりダウンロードしてご使用ください。
https://27.fileport-sample.example/0911-a84c27be5190f3d6e4ab07c2f9d8b3e15
PASS:qvrm
もう少し提案が見たいため、延長させて頂きます。
参考サイトを無視した少し奇抜なアイデアも見てみたいです。
■ 選んだ理由

院内で検討の上、決定致しました。
修正等も快諾いただき大変助かりました。

■ 提案者全員のお礼・コメント

皆様たくさんのご提案ありがとうございました。

```html
<!DOCTYPE html>
<html lang="ja">
<head>
<meta charset="utf-8">
<title>楓町デンタルクリニック</title>
<link rel="stylesheet" href="https://fonts.googleapis.com/css2?family=Cormorant+Garamond:wght@400;500&family=Noto+Serif+JP:wght@400;500;600&family=Noto+Sans+JP:wght@400;500&display=swap">
<style>
:root{
  --brown:#7d6446;
  --gold:#b8955e;
  --gold-soft:#d9c39c;
  --ink:#4a4038;
  --muted:#8b8178;
  --beige:#f3eee7;
  --beige-deep:#e9e1d6;
  --white:#fff;
  --line:#ddd3c5;
  --serif:"Noto Serif JP",serif;
  --en:"Cormorant Garamond",serif;
  --sans:"Noto Sans JP",sans-serif;
}
*{box-sizing:border-box;margin:0;padding:0}
html,body{width:1200px;height:5048px;overflow:hidden}
body{background:var(--white);color:var(--ink);font-family:var(--serif);font-size:13px;line-height:1.9;position:relative}
.section{position:absolute;left:0;width:1200px}
.abs{position:absolute}
.photo{position:absolute}
.en-title{font-family:var(--en);font-size:40px;letter-spacing:.12em;color:var(--ink);line-height:1;font-weight:400}
.jp-sub{font-size:11px;color:var(--gold);letter-spacing:.1em;margin-top:8px}
.btn{display:inline-block;background:var(--brown);color:#fff;font-size:12px;letter-spacing:.1em;padding:10px 0;width:180px;text-align:center}
.btn::after{content:" ›"}
p.body{font-size:12.5px;line-height:2.1;color:var(--ink)}

/* hero */
.hero{top:0;height:540px;background:linear-gradient(180deg,#f7f4ef,#efe9e0)}
.hero-photo{left:0;top:0;width:620px;height:540px;background:linear-gradient(135deg,#e8dccd,#cbb9a3 60%,#d8cbbb)}
.logo{left:40px;top:30px;font-family:var(--en);font-size:26px;letter-spacing:.1em;color:var(--ink);line-height:1.05;font-weight:500}
.logo small{display:block;font-size:11px;letter-spacing:.3em}
.header-tel{right:60px;top:0;width:228px;height:50px;background:#fff;padding:6px 14px;font-family:var(--sans)}
.header-tel b{font-size:17px;font-weight:500;letter-spacing:.05em;display:block;line-height:1.3}
.header-tel span{font-size:10px;color:var(--muted)}
.menu-btn{right:0;top:0;width:60px;height:50px;background:var(--brown);display:flex;flex-direction:column;justify-content:center;align-items:center;gap:5px}
.menu-btn i{display:block;width:22px;height:1px;background:#fff}
.hero-copy{left:700px;top:262px;font-size:25px;letter-spacing:.12em;line-height:2;font-weight:500}
.hero-copy .l1{padding-left:60px;display:block}

/* news */
.news{left:240px;top:540px;width:800px;height:86px;background:#fff;box-shadow:0 4px 24px rgba(120,100,70,.1);display:flex;align-items:center;padding:0 30px;z-index:2}
.news .head{width:150px}
.news .head .en-title{font-size:26px}
.news ul{list-style:none;flex:1;font-size:10.5px;line-height:1.9}
.news ul time{color:var(--gold);margin-right:16px;font-family:var(--sans)}
.news .btn{width:150px;font-size:11px}

/* concept */
.concept{top:626px;height:560px}
.concept .title{left:160px;top:112px}
.concept-photo{left:0;top:196px;width:600px;height:340px;background:linear-gradient(120deg,#c7d6df,#e6d9c9 55%,#d3c0a8)}
.concept h2{left:640px;top:150px;font-size:24px;font-weight:500;letter-spacing:.08em;line-height:1.7}
.concept .text{left:640px;top:250px;width:520px}
.concept .btn{left:640px;top:440px;position:absolute}

/* feature */
.feature{top:1186px;height:1090px;background:var(--beige)}
.feature .title{right:160px;top:86px;text-align:right}
.f-card{position:absolute;width:420px}
.f-card .ph{height:270px;position:relative}
.f-card .num{position:absolute;right:10px;top:6px;font-family:var(--en);font-size:40px;color:#fff;opacity:.85}
.f-card .txt{background:#fff;padding:22px 26px;height:200px}
.f-card h3{font-size:16px;color:var(--brown);font-weight:500;letter-spacing:.06em;margin-bottom:10px;border-left:3px solid var(--gold);padding-left:10px;line-height:1.4}
.f-card p{font-size:11.5px;line-height:1.95}

/* band */
.interior{top:2296px;height:284px;background:linear-gradient(90deg,#b89d7c,#e8ddce 40%,#d2bfa5 70%,#a88c6c)}

/* services */
.services{top:2580px;height:620px;background:linear-gradient(180deg,#fff,#f6f3ef)}
.services .title{left:0;width:1200px;top:64px;text-align:center}
.svc-grid{position:absolute;left:230px;top:180px;width:740px;display:grid;grid-template-columns:repeat(4,1fr);row-gap:30px}
.svc{text-align:center}
.svc .ic{width:104px;height:104px;border-radius:50%;background:#fff;border:1px solid var(--line);margin:0 auto 10px;display:flex;align-items:center;justify-content:center}
.svc span{font-size:11px;line-height:1.6;display:block}

/* blog */
.blog{top:3200px;height:430px;background:linear-gradient(90deg,#fbf4e8,#fff 40%)}
.blog .title{left:200px;top:0}
.arrows{right:160px;top:4px;display:flex;gap:12px}
.arrows i{width:34px;height:34px;border-radius:50%;border:1px solid var(--ink);display:flex;align-items:center;justify-content:center;font-style:normal;font-size:14px}
.arrows i.on{background:var(--ink);color:#fff}
.blog-track{left:-150px;top:100px;display:flex;gap:24px}
.b-card{width:236px}
.b-card .ph{height:156px}
.b-card p{font-size:11px;line-height:1.7;margin-top:10px}
.blog .btn{left:600px;top:348px;position:absolute}

/* recruit */
.recruit{top:3630px;height:520px;background:linear-gradient(120deg,#cfc8bf,#e9e4dd 50%,#c2b8ab)}
.recruit .box{left:240px;top:110px;width:800px;height:260px;background:rgba(255,255,255,.92);text-align:center;padding-top:40px}
.recruit .box p{font-size:11.5px;line-height:2;margin:18px auto 22px;width:620px}

/* faq/contact */
.links{top:4150px;height:120px;display:flex}
.links a{flex:1;display:flex;flex-direction:column;align-items:center;justify-content:center;color:#fff;text-decoration:none}
.links a .en-title{color:#fff;font-size:34px}
.links a .jp-sub{color:#f1e6d5}
.links .faq{background:linear-gradient(90deg,#4c3f33,#6b5a48)}
.links .contact{background:linear-gradient(90deg,#6b5a48,#4e4236)}

/* map */
.map{top:4270px;height:170px;background:linear-gradient(135deg,#e6ebe8,#dfe4e6 50%,#e9e6df)}

/* footer info */
.f-info{top:4440px;height:290px;background:#fff}
.f-info .logo{left:160px;top:50px}
.f-info .tel{left:460px;top:170px;position:absolute;border:1px solid var(--ink);width:250px;padding:4px 0;text-align:center;font-family:var(--sans);font-size:18px}
.f-info .name{left:460px;top:36px;font-size:15px;font-weight:500}
.f-info .addr{left:460px;top:66px;font-size:10.5px;line-height:1.9}
.f-info .btn{left:460px;top:220px;position:absolute;width:250px;font-size:11px;padding:6px 0}
.hours{left:760px;top:50px;border-collapse:collapse;font-size:10.5px;font-family:var(--sans)}
.hours th,.hours td{border-bottom:1px solid var(--line);padding:7px 10px;text-align:center;font-weight:400}
.hours td:first-child{text-align:left}
.dot{color:var(--gold)}
.hours-note{left:760px;top:170px;font-size:10.5px;line-height:1.9}

/* sitemap */
.f-nav{top:4730px;height:318px;background:var(--beige-deep)}
.nav-cols{left:160px;top:46px;display:flex;gap:50px;font-size:10.5px;line-height:2.3}
.nav-cols ul{list-style:none}
.nav-cols li::before{content:"› ";color:var(--gold)}
.copy{right:40px;bottom:20px;font-size:9px;color:var(--muted);font-family:var(--sans)}
</style>
</head>
<body>

<header class="section hero">
  <div class="photo hero-photo" role="img" aria-label="歯磨きをする子どもの写真"></div>
  <div class="abs logo">KAEDEMACHI<small>DENTAL</small></div>
  <div class="abs header-tel"><b>☎ 090-5550-2184</b><span>診療時間 9:00〜18:00</span></div>
  <div class="abs menu-btn"><i></i><i></i><i></i></div>
  <h1 class="abs hero-copy"><span class="l1">一人ひとりに合わせた</span>質の高い歯科医療を提供しています</h1>
</header>

<div class="abs news">
  <div class="head"><div class="en-title">NEWS</div><div class="jp-sub">お知らせ</div></div>
  <ul>
    <li><time>2021.05.01</time>「夏季休診日のお知らせ」を掲載しました</li>
    <li><time>2021.04.15</time>ホームページをリニューアルしました</li>
    <li><time>2021.04.01</time>オンライン予約の受付を開始しました</li>
  </ul>
  <a class="btn">お知らせ一覧</a>
</div>

<section class="section concept">
  <div class="abs title"><div class="en-title">CONCEPT</div><div class="jp-sub">コンセプト</div></div>
  <div class="photo concept-photo" role="img" aria-label="歯科医師と子どもと母親の診療風景の写真"></div>
  <h2 class="abs">地域と社会に貢献できる<br>歯科医院であり続けたい</h2>
  <div class="abs text"><p class="body">当院は地域の皆さまのお口の健康を守るため、丁寧な説明と痛みに配慮した治療を心がけています。小さなお子さまからご高齢の方まで、安心して通える歯科医院を目指しています。<br>一人ひとりのお悩みに寄り添い、長く健康な歯を保つためのお手伝いをいたします。</p></div>
  <a class="btn">当院について</a>
</section>

<section class="section feature">
  <div class="abs title"><div class="en-title">FEATURE</div><div class="jp-sub">当院の特徴</div></div>
  <div class="f-card" style="left:160px;top:190px">
    <div class="ph" role="img" aria-label="落ち着いた待合室の写真" style="background:linear-gradient(135deg,#a68a67,#d9c6a8)"><span class="num">01</span></div>
    <div class="txt"><h3>居心地のいい空間の提供</h3><p>木の温もりを感じる院内で、リラックスして治療を受けていただけます。待合室は広く、プライバシーに配慮した個室診療室もご用意しています。</p></div>
  </div>
  <div class="f-card" style="left:620px;top:190px">
    <div class="ph" role="img" aria-label="診療室の設備の写真" style="background:linear-gradient(135deg,#8f7a64,#cfc3b4)"><span class="num">02</span></div>
    <div class="txt"><h3>最先端の技術と安心の設備</h3><p>精密な診断を行うための機器を導入し、より正確で負担の少ない治療を行います。衛生管理も徹底し、安心して通える環境を整えています。</p></div>
  </div>
  <div class="f-card" style="left:160px;top:660px">
    <div class="ph" role="img" aria-label="夜の医院外観の写真" style="background:linear-gradient(180deg,#3e4350,#8b7a66)"><span class="num">03</span></div>
    <div class="txt"><h3>このテキストはダミーです</h3><p>ここには当院の特徴を説明する文章が入ります。患者さまに分かりやすく伝わるよう、簡潔な言葉でご紹介する予定です。</p></div>
  </div>
  <div class="f-card" style="left:620px;top:660px">
    <div class="ph" role="img" aria-label="個室の診療チェアの写真" style="background:linear-gradient(135deg,#9c8266,#ddd2c4)"><span class="num">04</span></div>
    <div class="txt"><h3>このテキストはダミーです</h3><p>ここには当院の特徴を説明する文章が入ります。患者さまに分かりやすく伝わるよう、簡潔な言葉でご紹介する予定です。</p></div>
  </div>
</section>

<div class="section interior" role="img" aria-label="院内の受付と待合スペースの写真"></div>

<section class="section services">
  <div class="abs title"><div class="en-title">SERVICES</div><div class="jp-sub">診療案内</div></div>
  <div class="svc-grid">
    <div class="svc"><div class="ic"><svg width="44" height="44" viewBox="0 0 44 44" fill="none" stroke="#b8955e" stroke-width="1.5"><path d="M12 10c4-3 8 0 10 0s6-3 10 0c4 4 1 12 0 16-1 6-3 10-5 10s-2-8-5-8-3 8-5 8-4-4-5-10c-1-4-4-12 0-16z"/></svg></div><span>銀歯から<br>自然な白い歯へ</span></div>
    <div class="svc"><div class="ic"><svg width="44" height="44" viewBox="0 0 44 44" fill="none" stroke="#b8955e" stroke-width="1.5"><rect x="8" y="12" width="28" height="22" rx="2"/><path d="M16 12v-4h12v4"/></svg></div><span>歯医者に<br>いけなくなった方へ</span></div>
    <div class="svc"><div class="ic"><svg width="44" height="44" viewBox="0 0 44 44" fill="none" stroke="#b8955e" stroke-width="1.5"><rect x="6" y="14" width="32" height="16" rx="8"/><path d="M14 14v16M22 14v16M30 14v16"/></svg></div><span>歯の色を全体的に<br>白くしたい方へ</span></div>
    <div class="svc"><div class="ic"><svg width="44" height="44" viewBox="0 0 44 44" fill="none" stroke="#b8955e" stroke-width="1.5"><path d="M10 26c6 8 18 8 24 0M14 20h16"/></svg></div><span>口臭が気になる・<br>歯茎に違和感がある</span></div>
    <div class="svc"><div class="ic"><svg width="44" height="44" viewBox="0 0 44 44" fill="none" stroke="#b8955e" stroke-width="1.5"><path d="M6 22h32M10 16v12M18 16v12M26 16v12M34 16v12"/></svg></div><span>歯並びを<br>整えたい方へ</span></div>
    <div class="svc"><div class="ic"><svg width="44" height="44" viewBox="0 0 44 44" fill="none" stroke="#b8955e" stroke-width="1.5"><path d="M14 10c3-2 6 0 8 0s5-2 8 0c3 3 1 9 0 12H14c-1-3-3-9 0-12zM18 26h8M19 30h6M20 34h4"/></svg></div><span>歯が失って<br>しまった方へ</span></div>
    <div class="svc"><div class="ic"><svg width="44" height="44" viewBox="0 0 44 44" fill="none" stroke="#b8955e" stroke-width="1.5"><path d="M12 10c4-3 8 0 10 0s6-3 10 0c4 4 1 12 0 16-1 6-3 10-5 10s-2-8-5-8-3 8-5 8-4-4-5-10c-1-4-4-12 0-16z"/><circle cx="26" cy="16" r="2.5"/></svg></div><span>虫歯になって<br>しまった方へ</span></div>
    <div class="svc"><div class="ic"><svg width="44" height="44" viewBox="0 0 44 44" fill="none" stroke="#b8955e" stroke-width="1.5"><path d="M22 8l12 5v9c0 7-5 12-12 14-7-2-12-7-12-14v-9z"/><path d="M17 22l4 4 7-7"/></svg></div><span>お子様の歯を<br>守りたい方へ</span></div>
  </div>
</section>

<section class="section blog">
  <div class="abs title"><div class="en-title">BLOG</div><div class="jp-sub">ブログ</div></div>
  <div class="abs arrows"><i>‹</i><i class="on">›</i></div>
  <div class="abs blog-track">
    <div class="b-card"><div class="ph" role="img" aria-label="歯の模型の写真" style="background:linear-gradient(135deg,#e9c8c4,#f4ece6)"></div><p>ブログのタイトルが入ります。<br>ブログのタイトルです</p></div>
    <div class="b-card"><div class="ph" role="img" aria-label="歯ブラシの写真" style="background:linear-gradient(135deg,#dfe6e4,#f3efe8)"></div><p>ブログのタイトルが入ります。<br>ブログのタイトルです</p></div>
    <div class="b-card"><div class="ph" role="img" aria-label="診療器具の写真" style="background:linear-gradient(135deg,#cfd6da,#eef0f0)"></div><p>ブログのタイトルが入ります。<br>ブログのタイトルです</p></div>
    <div class="b-card"><div class="ph" role="img" aria-label="歯の模型と器具の写真" style="background:linear-gradient(135deg,#e9ecef,#c9d3d9)"></div><p>ブログのタイトルが入ります。<br>ブログのタイトルです</p></div>
    <div class="b-card"><div class="ph" role="img" aria-label="模型の歯の写真" style="background:linear-gradient(135deg,#e4e9ec,#f6f4f0)"></div><p>ブログのタイトルが入ります。<br>ブログのタイトルです</p></div>
    <div class="b-card"><div class="ph" role="img" aria-label="歯科治療の写真" style="background:linear-gradient(135deg,#b9d7de,#eaf1f2)"></div><p>ブログのタイトルが入ります。<br>ブログのタイトルです</p></div>
  </div>
  <a class="btn" style="transform:translateX(-50%)">ブログ一覧</a>
</section>

<section class="section recruit" role="img" aria-label="院内スタッフの背景写真">
  <div class="abs box">
    <div class="en-title">RECRUIT</div><div class="jp-sub">求人情報</div>
    <p>当院では一緒に働くスタッフを募集しています。地域の皆さまの健康を支えるやりがいのある職場です。経験の有無は問いません。まずはお気軽にご応募ください。</p>
    <a class="btn">求人情報</a>
  </div>
</section>

<nav class="section links">
  <a class="faq" role="img" aria-label="よくあるご質問の背景写真"><span class="en-title">FAQ</span><span class="jp-sub">よくあるご質問</span></a>
  <a class="contact" role="img" aria-label="お問い合わせの背景写真"><span class="en-title">CONTACT</span><span class="jp-sub">お問い合わせ</span></a>
</nav>

<div class="section map" role="img" aria-label="医院周辺の地図"></div>

<footer>
  <section class="section f-info">
    <div class="abs logo">KAEDEMACHI<small>DENTAL</small></div>
    <div class="abs name">楓町デンタルクリニック</div>
    <div class="abs addr">〒000-0000<br>楓町一丁目2番3号 楓町ビル1階<br>楓町駅より徒歩3分</div>
    <div class="tel">☎ 090-5550-2184</div>
    <a class="btn">WEB予約</a>
    <table class="abs hours">
      <tr><th>診療時間</th><th>月</th><th>火</th><th>水</th><th>木</th><th>金</th><th>土</th><th>日</th></tr>
      <tr><td>09:00-12:30</td><td class="dot">●</td><td class="dot">●</td><td class="dot">●</td><td class="dot">●</td><td class="dot">●</td><td class="dot">●</td><td>−</td></tr>
      <tr><td>14:00-18:00</td><td class="dot">●</td><td class="dot">●</td><td class="dot">●</td><td>−</td><td class="dot">●</td><td class="dot">●</td><td>−</td></tr>
    </table>
    <div class="abs hours-note">休診日：木曜午後・日曜・祝日<br>P 駐車場あり</div>
  </section>
  <section class="section f-nav">
    <div class="abs nav-cols">
      <ul><li>HOME</li><li>当院について</li><li>医院紹介</li><li>スタッフ紹介</li></ul>
      <ul><li>初めての方へ</li><li>お知らせ</li><li>ブログ</li></ul>
      <ul><li>銀歯から自然な白い歯へ</li><li>歯医者にいけなくなった方へ</li><li>歯の色を全体的に白くしたい方へ</li><li>口臭が気になる・歯茎に違和感がある</li></ul>
      <ul><li>歯並びを整えたい方へ</li><li>歯が失ってしまった方へ</li><li>虫歯になってしまった方へ</li><li>お子様の歯を守りたい方へ</li></ul>
      <ul><li>求人情報</li><li>よくあるご質問</li><li>お問い合わせ</li></ul>
    </div>
    <div class="abs copy">© KAEDEMACHI DENTAL CLINIC</div>
  </section>
</footer>

</body>
</html>
```